Postcard Design

Need postcard design for dental office. The doctor is returning to the office after a few months medical leave and he wants a postcard to be mailed to patients and families in the surrounding area to create new patients. We have attached a rough sketch of the information we would like to include on the postcard along with color selection but are open to additional artwork or design to improve the overall look. We are also including a photo of the dentist for the front of the postcard. We plan to have the metered postage through Plentomark if possible so please let me know how that works because I'm assuming that will need to be included in the design. I am also attaching a sample of a postcard that the dentist received in the mail from a Corbridge doctor and would like his postcard to resemble this layout. The postcard needs to 8.5 x 5.5; I believe this is called the oversized selection for Plentomark and we are planning to have them do the printing. Please verify you did receive four attached files including photo, front sketch, back sketch, and actual postcard example.

Thank you,
Marlene Tofsky

```html
<!DOCTYPE html>
<html lang="en">
<head>
<meta charset="utf-8">
<title>General Dentist Postcard</title>
<link rel="stylesheet" href="https://fonts.googleapis.com/css2?family=Marcellus&family=Lato:wght@400;700&display=swap">
<style>
  :root {
    --page: #eeeae4;
    --card-light: #e1f1f7;
    --white: #ffffff;
    --ink: #2b2f8f;
    --navy-deep: #06112f;
    --navy-mid: #0d2c7a;
    --sky: #7ccdf3;
    --photo-dark: #1c1d22;
    --photo-light: #cfd0d3;
  }
  * { box-sizing: border-box; margin: 0; padding: 0; }
  html, body { width: 1016px; height: 1200px; overflow: hidden; }
  body {
    background: var(--page);
    position: relative;
    font-family: "Marcellus", "Optima", sans-serif;
    color: var(--ink);
  }
  .postcard {
    position: absolute;
    width: 793px;
    height: 513px;
    background: var(--white);
    box-shadow: 6px 8px 14px rgba(0,0,0,0.22);
    overflow: hidden;
  }
  .postcard--front { left: 33px; top: 41px; }
  .postcard--back { left: 166px; top: 622px; }

  /* Front */
  .front-field {
    position: absolute; left: 0; top: 0; width: 793px; height: 424px;
    background: var(--card-light);
  }
  .doctor-photo { position: absolute; left: 0; top: 0; }
  .title {
    position: absolute; font-size: 26px; line-height: 33px; letter-spacing: 0.5px;
  }
  .front-field .title { left: 637px; top: 28px; }
  .front-tagline {
    position: absolute; left: 320px; width: 446px; top: 135px;
    text-align: center; font-size: 20px; white-space: nowrap;
  }
  .doctor-name {
    position: absolute; left: 300px; width: 458px; top: 204px;
    text-align: center; font-size: 24px; letter-spacing: 0.3px; white-space: nowrap;
  }
  .front-phone {
    position: absolute; left: 320px; width: 418px; top: 244px;
    display: flex; justify-content: center; align-items: center; gap: 8px;
    font-size: 27px; font-weight: 700; font-family: "Lato", sans-serif; letter-spacing: -0.3px;
  }
  .office {
    position: absolute; left: 520px; width: 264px; top: 320px;
    text-align: center; font-family: "Lato", sans-serif; font-size: 15px; line-height: 21px;
    white-space: nowrap;
  }
  .office-city { margin-bottom: 9px; }
  .band {
    position: absolute; left: 0;
    background: linear-gradient(90deg, var(--navy-deep) 0%, var(--navy-deep) 40%, var(--navy-mid) 55%, var(--navy-deep) 80%, var(--navy-deep) 100%);
    color: var(--white);
  }
  .postcard--front .band { top: 424px; width: 793px; height: 72px; }
  .band-headline {
    position: absolute; left: 31px; top: 17px; font-size: 34px; letter-spacing: 0.3px; white-space: nowrap;
  }
  .band-info {
    position: absolute; left: 479px; width: 300px; top: 17px;
    text-align: center; font-family: "Lato", sans-serif; font-size: 14px; line-height: 19px;
    white-space: nowrap;
  }
  .stripe { position: absolute; left: 0; background: var(--sky); }
  .postcard--front .stripe { top: 496px; width: 793px; height: 5px; }

  /* Back */
  .back-panel {
    position: absolute; left: 0; top: 0; width: 397px; height: 513px;
    background: var(--card-light);
  }
  .postcard--back .band { top: 0; width: 397px; height: 110px;
    background: linear-gradient(90deg, var(--navy-deep) 0%, var(--navy-mid) 55%, var(--navy-deep) 100%); }
  .back-band-text {
    position: absolute; left: 0; width: 397px; top: 35px;
    text-align: center; font-size: 19px; line-height: 26px; white-space: nowrap;
  }
  .postcard--back .stripe { top: 110px; width: 397px; height: 17px; }
  .bio {
    position: absolute; left: 37px; width: 345px; top: 170px;
    font-size: 19.5px; line-height: 31.5px;
  }
  .bio p + p { margin-top: 22px; }
  .postcard--back .title { left: 422px; top: 31px; font-size: 28px; line-height: 36px; }
</style>
</head>
<body>
  <section class="postcard postcard--front">
    <div class="front-field">
      <svg class="doctor-photo" width="330" height="424" role="img" aria-label="Portrait photo of the dentist in a dark suit and tie">
        <defs>
          <linearGradient id="photoTone" x1="0" y1="0" x2="0" y2="1">
            <stop offset="0" stop-color="#cfd0d3"/>
            <stop offset="0.45" stop-color="#9a9ba0"/>
            <stop offset="0.6" stop-color="#1c1d22"/>
            <stop offset="1" stop-color="#1c1d22"/>
          </linearGradient>
        </defs>
        <path d="M0 0 H322 C282 120 268 300 317 424 H0 Z" fill="url(#photoTone)"/>
      </svg>
      <div class="title">GENERAL<br>DENTIST</div>
      <div class="front-tagline">Now Accepting Established and New Patients</div>
      <div class="doctor-name">ALAN R. WHITFORD, DDS, FAGD</div>
      <div class="front-phone">
        <svg width="24" height="24" viewBox="0 0 24 24" aria-hidden="true">
          <path fill="#2b2f8f" d="M6.6 10.8c1.4 2.8 3.8 5.1 6.6 6.6l2.2-2.2c.3-.3.7-.4 1-.2 1.1.4 2.3.6 3.6.6.6 0 1 .4 1 1V20c0 .6-.4 1-1 1C10.6 21 3 13.4 3 4c0-.6.4-1 1-1h3.5c.6 0 1 .4 1 1 0 1.3.2 2.5.6 3.6.1.3 0 .7-.2 1z"/>
        </svg>
        <span>555-014-2290</span>
      </div>
      <div class="office">
        <div class="office-city">HALBROOK</div>
        <div>4820 Larkmoor Ave, Ste B</div>
        <div>Halbrook, GA 30199</div>
        <div>555-014-2290</div>
      </div>
    </div>
    <div class="band">
      <div class="band-headline">NOW ACCEPTING PATIENTS</div>
      <div class="band-info">For more information, please call<br>555-014-2290 or visit DrWhitford.com</div>
    </div>
    <div class="stripe"></div>
  </section>

  <section class="postcard postcard--back">
    <div class="back-panel">
      <div class="band">
        <div class="back-band-text">Accepting Established and New Patients<br>call 555-014-2290 or visit DrWhitford.com</div>
      </div>
      <div class="stripe"></div>
      <div class="bio">
        <p>Alan R. Whitford DDS, FAGD, a native of Halbrook, Ga earned his Doctorate of Dental Surgery at Ridgemont University Dental School in Brantley.</p>
        <p>Dr. Whitford has been improving the dental health of patients in Western Georgia for over 25 years.</p>
      </div>
    </div>
    <div class="title">GENERAL<br>DENTIST</div>
  </section>
</body>
</html>
```